plumbers buisness card

A buisness card for a plumbing buisness
needs to have a water theme with navy blue, light blue and white
with an image of either a water drop, pipes, tools or something relating to plumbing and incorperating my buisness name as a logo

"Talcott Plumbing" is the words that need to stand out with "& gasfitting" to be smaller
Updates

spelling error on brief, "maintenance"
and also could you include my email m_talcott@nimbrel.com.au

Industry/Entity Type

Plumbing

Contact Information for Business Card

Talcott Plumbing & Gasfitting

myles talcott
0492315806

specialising in
-new homes
-maitenance
-renovations

license no.
-73846

```html
<!DOCTYPE html>
<html lang="en">
<head>
<meta charset="utf-8">
<title>Talcott Plumbing &amp; Gasfitting — Business Card</title>
<link rel="stylesheet" href="https://fonts.googleapis.com/css2?family=Open+Sans:wght@400&family=PT+Sans:wght@400;700&display=swap">
<style>
  :root {
    --stage: #7f7f7d;
    --label: #ffffff;
    --navy: #34506f;
    --steel-blue: #5a7a9e;
    --slate: #47668a;
    --chrome-light: #e4e7eb;
    --chrome-mid: #b9c0c9;
    --chrome-dark: #8e99a6;
    --mist: #e9edf1;
    --mist-blue: #8193ab;
    --mist-light: #f5f6f8;
    --white: #ffffff;
    --ink: #2e2e30;
  }
  * { margin: 0; padding: 0; box-sizing: border-box; }
  html, body {
    width: 1200px; height: 439px; overflow: hidden;
    background: var(--stage);
  }
  .presentation { position: relative; width: 1200px; height: 439px; }

  .side-label {
    position: absolute; top: 18px;
    font-family: "Open Sans", sans-serif; font-weight: 400;
    font-size: 31px; color: var(--label);
  }
  .side-label--front { left: 267px; }
  .side-label--back { left: 846px; }

  .card {
    position: absolute; top: 94px; height: 304px; overflow: hidden;
    font-family: "PT Sans", sans-serif;
  }
  .card--front { left: 28px; width: 529px; }
  .card--back { left: 627px; width: 532px; }

  .card__photo { position: absolute; inset: 0; width: 100%; height: 100%; }

  .brand { position: absolute; left: 19px; top: 38px; }
  .card--back .brand { left: 22px; }
  .brand__name {
    font-weight: 700; font-size: 23.5px; line-height: 1;
    color: var(--white); letter-spacing: 0.1px;
  }
  .brand__trade {
    margin: 10px 0 0 58px;
    font-size: 16px; line-height: 1; color: var(--white);
  }

  .contact {
    position: absolute; left: 19px; top: 189px;
    color: var(--white);
  }
  .contact__person { font-size: 16.5px; line-height: 1; }
  .contact__phone { font-size: 13px; }
  .contact__heading { margin-top: 10px; font-weight: 700; font-size: 13.5px; line-height: 1.2; }
  .contact__services { font-size: 14.5px; line-height: 1.2; }
  .contact__email { margin-top: 9px; font-size: 13.5px; line-height: 1.3; }
  .contact__licence { font-size: 13.5px; line-height: 1.3; }
  .label-bold { font-weight: 700; }

  .back-email {
    position: absolute; left: 22px; top: 267px;
    font-size: 13.5px; color: var(--ink);
  }
</style>
</head>
<body>
<main class="presentation">
  <h2 class="side-label side-label--front">Front</h2>
  <h2 class="side-label side-label--back">Back</h2>

  <section class="card card--front">
    <svg class="card__photo" viewBox="0 0 529 304" preserveAspectRatio="none" aria-hidden="true">
      <defs>
        <linearGradient id="front-tone" x1="0" y1="0" x2="1" y2="1">
          <stop offset="0" stop-color="var(--navy)"/>
          <stop offset="0.55" stop-color="var(--slate)"/>
          <stop offset="1" stop-color="var(--steel-blue)"/>
        </linearGradient>
        <linearGradient id="front-pipes" x1="0" y1="0" x2="1" y2="0.4">
          <stop offset="0" stop-color="var(--chrome-light)"/>
          <stop offset="0.5" stop-color="var(--chrome-mid)"/>
          <stop offset="1" stop-color="var(--chrome-dark)"/>
        </linearGradient>
      </defs>
      <rect width="529" height="304" fill="url(#front-tone)"/>
      <path class="card__pipes" role="img" aria-label="Photograph of chrome plumbing pipes bending over a blue background with a red pipe wrench"
            d="M215,0 H529 V304 H320 V190 Q320,150 280,150 H215 Z" fill="url(#front-pipes)"/>
    </svg>
    <div class="brand">
      <p class="brand__name">Talcott Plumbing</p>
      <p class="brand__trade">&amp; Gasfitting</p>
    </div>
    <div class="contact">
      <p class="contact__person">Myles Talcott <span class="contact__phone">: 0492315806</span></p>
      <p class="contact__heading">Specialising in :</p>
      <p class="contact__services">New homes | Maintenance | Renovations</p>
      <p class="contact__email"><span class="label-bold">e-mail :</span> m_talcott@nimbrel.com.au</p>
      <p class="contact__licence">license no. -73846</p>
    </div>
  </section>

  <section class="card card--back">
    <svg class="card__photo" viewBox="0 0 532 304" preserveAspectRatio="none" aria-hidden="true">
      <defs>
        <linearGradient id="back-tone" x1="0" y1="0" x2="0" y2="1">
          <stop offset="0" stop-color="var(--mist-blue)"/>
          <stop offset="0.55" stop-color="var(--mist-blue)"/>
          <stop offset="0.62" stop-color="var(--mist)"/>
          <stop offset="1" stop-color="var(--mist)"/>
        </linearGradient>
        <linearGradient id="back-pipes" x1="0" y1="0" x2="1" y2="0.4">
          <stop offset="0" stop-color="var(--mist-light)"/>
          <stop offset="1" stop-color="var(--mist)"/>
        </linearGradient>
      </defs>
      <rect width="532" height="304" fill="url(#back-tone)"/>
      <path class="card__pipes" role="img" aria-label="Faded photograph of chrome plumbing pipes on a pale background"
            d="M222,0 H532 V304 H0 V170 H280 Q310,170 310,140 Q310,120 222,120 Z" fill="url(#back-pipes)"/>
    </svg>
    <div class="brand">
      <p class="brand__name">Talcott Plumbing</p>
      <p class="brand__trade">&amp; Gasfitting</p>
    </div>
    <p class="back-email"><span class="label-bold">e-mail :</span> m_talcott@nimbrel.com.au</p>
  </section>
</main>
</body>
</html>
```